Local Pharmacy Drug Store looking for graphic store front design

Hello Everyone,
We are a local Pharmacy Drug Store looking for a Graphic Storefront design. We're a neighborhood pharmacy who serves all ages but serves a large portion of elderly patients.
I am attaching a image of the storefront (Sunmarsh store front.png), We are looking to have the whole right window side redesigned, so the majority of the work will happen there.
In regards to design I am attaching an example of what we are looking for (I.E Storefront Example.png). We want to have the name "Sun Marsh Pharmacy" Brightly displayed with words such as "Free Delivery" and "Most Insurance Accepted" included in smaller texts just like the example attached. We could also add images such as Tillpoint Card and a wheelchair. Be aware that we are looking for a design that has depth with color and background images. Please feel free to add any other context that would be fitting for a local neighborhood pharmacy.
Keep in mind that this design will only cover the right side window as shown in the "Sun Marsh Storefront" image

```html
<!DOCTYPE html>
<html lang="en">
<head>
<meta charset="utf-8">
<title>Sun Marsh Pharmacy – Window Graphic</title>
<link rel="stylesheet" href="https://fonts.googleapis.com/css2?family=Montserrat:wght@400;600&family=Tinos:wght@700&display=swap">
<style>
  :root {
    --backdrop: #5fcbdc;
    --brand-blue: #3380cc;
    --paper: #ffffff;
    --brand-red: #e0203f;
    --mortar-light: #f1ede2;
    --mortar-shade: #d6ccb4;
  }
  * { margin: 0; padding: 0; box-sizing: border-box; }
  html, body {
    width: 1200px;
    height: 1200px;
    overflow: hidden;
    background: var(--backdrop);
  }
  .window-graphic {
    position: absolute;
    left: 100px;
    top: 133px;
    width: 1000px;
    height: 934px;
    box-shadow: 0 6px 14px rgba(0, 0, 0, 0.25);
  }
  .window-graphic svg { display: block; width: 100%; height: 100%; }
  .headline {
    font-family: "Tinos", "Times New Roman", serif;
    font-weight: 700;
    font-size: 60px;
    fill: var(--paper);
  }
  .tagline {
    font-family: "Montserrat", Arial, sans-serif;
    font-weight: 400;
    font-size: 25px;
    fill: var(--paper);
  }
  .service-list {
    font-family: "Montserrat", Arial, sans-serif;
    font-weight: 400;
    font-size: 25px;
    fill: var(--brand-blue);
  }
  .brand-mark-name {
    font-family: "Montserrat", Arial, sans-serif;
    font-weight: 600;
    font-size: 20px;
    fill: var(--paper);
  }
</style>
</head>
<body>
  <main class="window-graphic">
    <svg viewBox="0 0 622 581" xmlns="http://www.w3.org/2000/svg">
      <defs>
        <radialGradient id="mortar-tone" cx="0.5" cy="0.55" r="0.55">
          <stop offset="0" stop-color="var(--mortar-light)"/>
          <stop offset="1" stop-color="var(--mortar-shade)"/>
        </radialGradient>
      </defs>

      <rect class="panel-background" width="622" height="581" fill="var(--brand-blue)"/>

      <path class="white-wave" fill="var(--paper)"
        d="M0,350 C120,355 200,330 300,280 C380,240 420,228 460,234 C530,242 580,300 622,370
           L622,530 C580,560 520,585 470,580 C380,570 300,530 200,524 C120,520 60,522 0,524 Z"/>

      <g class="brand-mark">
        <circle cx="525" cy="72" r="22" fill="var(--brand-red)"/>
        <text class="brand-mark-name" x="525" y="125" text-anchor="middle">Sun Marsh</text>
      </g>

      <text class="headline" x="18" y="88">SUN</text>
      <text class="headline" x="18" y="153">MARSH</text>
      <text class="headline" x="18" y="218">PHARMACY</text>

      <text class="tagline" x="19" y="279">MOST INSURANCE</text>
      <text class="tagline" x="19" y="309">ACCEPTED</text>

      <text class="service-list" x="19" y="407">FREE DELIVERY</text>
      <text class="service-list" x="19" y="444">TILLPOINT CARD</text>
      <text class="service-list" x="19" y="480">WHEELCHAIR</text>

      <g role="img" aria-label="Photo of a white ceramic mortar with a wooden-handled pestle">
        <ellipse cx="470" cy="440" rx="100" ry="90" fill="url(#mortar-tone)"/>
      </g>
    </svg>
  </main>
</body>
</html>
```